Flyer für Veranstaltungstechnik-Unternehmen
Velmira suchte ein neues Design in der Kategorie Flyer und hat ein Projekt auf grafikwunsch.de gestartet.
Zielgruppe
VERANSTALTUNGSTECHNIK
Aufgabenstellung
Wir haben diesen Flyer erhalten, finden ihn aber nicht ansprechend, sehr altmodisch und möchten einen klar strukturierten modernen Flyer.
DIN A5 „Heft“ – Und das Profil als „Einleger“. Sollte dementsprechend ca. 1 cm umlaufend kleiner sein.
Der Flyer soll sich an dem Design der Webseite orientieren!

```html
<!DOCTYPE html>
<html lang="de">
<head>
<meta charset="utf-8">
<title>Leistungen auf einen Blick</title>
<link href="https://fonts.googleapis.com/css2?family=Raleway:wght@700&family=Source+Sans+3:wght@400&display=swap" rel="stylesheet">
<style>
  :root {
    --bg: #a7a7a7;
    --frame: #ffffff;
    --page: #0a0a0a;
    --accent: #8f78bb;
    --text: #f2f2f2;
  }
  * { margin: 0; padding: 0; box-sizing: border-box; }
  html, body { width: 1200px; height: 874px; overflow: hidden; }
  body { background: var(--bg); position: relative; font-family: "Source Sans 3", "Source Sans Pro", sans-serif; color: var(--text); }
  .sheet { position: absolute; top: 33px; width: 562px; height: 791px; background: var(--frame); }
  .sheet--left { left: 32px; }
  .sheet--right { left: 600px; }
  .sheet__photo {
    position: absolute; left: 8px; top: 8px; width: 546px; height: 775px;
  }
  .sheet--left .sheet__photo {
    background:
      radial-gradient(ellipse 200px 120px at 480px 230px, rgba(255,255,255,.85), rgba(255,255,255,.2) 45%, rgba(0,0,0,0) 75%),
      linear-gradient(180deg, #111 0%, #2a2a2a 30%, #161616 55%, var(--page) 75%);
  }
  .sheet--right .sheet__photo {
    background:
      radial-gradient(ellipse 230px 130px at 90px 230px, rgba(255,255,255,.85), rgba(255,255,255,.2) 45%, rgba(0,0,0,0) 75%),
      linear-gradient(180deg, #151515 0%, #2c2c2c 30%, #171717 55%, var(--page) 75%);
  }
  .heading { position: absolute; left: 85px; top: 452px; }
  .heading__title { font-family: "Raleway", sans-serif; font-weight: 700; font-size: 24px; color: var(--accent); line-height: 1; letter-spacing: .2px; }
  .heading__sub { font-size: 19px; letter-spacing: 4.4px; line-height: 1; margin-top: 8px; }
  .services { list-style: none; position: absolute; }
  .services li { position: absolute; left: 0; font-size: 12.3px; line-height: 16px; white-space: nowrap; }
  .services .icon { position: absolute; width: 16px; height: 16px; top: 0; }
  .services--left { left: 85px; top: 0; }
  .services--left .icon { left: -29px; }
  .services--right { left: 665px; top: 0; }
  .services--right .icon { left: -30px; }
</style>
</head>
<body>
  <svg width="0" height="0" style="position:absolute">
    <symbol id="tools" viewBox="0 0 16 16">
      <path d="M2 14 L11 5" stroke="#8f78bb" stroke-width="2.4" stroke-linecap="round"/>
      <path d="M14 14 L5 5" stroke="#8f78bb" stroke-width="2.4" stroke-linecap="round"/>
      <path d="M9 2 L14 2 L14 5 L11 7 Z" fill="#8f78bb"/>
      <circle cx="4" cy="4" r="2.6" fill="#8f78bb"/>
    </symbol>
  </svg>

  <section class="sheet sheet--left">
    <div class="sheet__photo" role="img" aria-label="Schwarzweißfoto: Konzertpublikum vor hell angestrahlter Bühne"></div>
  </section>
  <section class="sheet sheet--right">
    <div class="sheet__photo" role="img" aria-label="Schwarzweißfoto: Publikum mit Smartphones vor Bühne mit Scheinwerfern"></div>
  </section>

  <header class="heading">
    <h1 class="heading__title">LEISTUNGEN</h1>
    <p class="heading__sub">auf einen Blick</p>
  </header>

  <ul class="services services--left">
    <li style="top:521px"><svg class="icon"><use href="#tools"/></svg>Vorplanung, Durchführung und Nachbereitung von Veranstaltungen</li>
    <li style="top:552px"><svg class="icon"><use href="#tools"/></svg>Koordination, Organisation und Planung sämtlicher Gewerke</li>
    <li style="top:583px"><svg class="icon"><use href="#tools"/></svg>Erstellen von Projekt-, Budget- und Terminplänen</li>
    <li style="top:615px"><svg class="icon"><use href="#tools"/></svg>Budgetierung aller Bereiche und Gewerke, auch auf Kundenseite und damit verbunden<br>die Prüfung aller Verträge, Angebote und Rechnungen im Rahmen der Veranstaltungen<br>(Third Party Audit)</li>
    <li style="top:678px"><svg class="icon"><use href="#tools"/></svg>Kommunikation mit allen Gewerken, der Location und den Behörden</li>
    <li style="top:709px"><svg class="icon"><use href="#tools"/></svg>Erstellen von Sicherheitskonzepten unter Einbeziehung von Sicherheitspersonal</li>
    <li style="top:740px"><svg class="icon"><use href="#tools"/></svg>Erstellung von Gefährdungsbeurteilungen für die zu betreuenden technischen Bereiche</li>
  </ul>

  <ul class="services services--right">
    <li style="top:498px"><svg class="icon"><use href="#tools"/></svg>Koordination, Abstimmung und Übernahme der logistischen Verantwortung für den<br>Messebereich</li>
    <li style="top:545px"><svg class="icon"><use href="#tools"/></svg>Übernahme des Verantwortlichen für Veranstaltungstechnik (Meister für<br>Veranstaltungstechnik)</li>
    <li style="top:592px"><svg class="icon"><use href="#tools"/></svg>Übernahme der Verantwortung als technischer Leiter für die Gesamtveranstaltung</li>
    <li style="top:623px"><svg class="icon"><use href="#tools"/></svg>Studioumbauten und Betreuung</li>
    <li style="top:654px"><svg class="icon"><use href="#tools"/></svg>Technische Betreuung Bühne und Licht</li>
    <li style="top:686px"><svg class="icon"><use href="#tools"/></svg>Koordination Dekorationsbau</li>
    <li style="top:717px"><svg class="icon"><use href="#tools"/></svg>Zeichnen aller veranstaltungsspezifischen Pläne (technisch und<br>sicherheitstechnisch)</li>
  </ul>
</body>
</html>
```